I want a business card that is going to show a creative spark but without limiting me to an industry. Something edgy but that wont go out of date. I want it state My business name Serafina Loire, profession - Professional Makeup Artist contact number and email

My service is to provide makeup services from bridal, fashion, photography, film, TV and so on. It is creative and different so i want that to be reflected.

I would like the card double sided.
Updates

 I would LOVE a background on my card something like this image... i can supply an image to be formed like this

Please use the image uploaded

Can we try using the image provided on one side of the card and then writing and details on the other side

Target Market(s)

I am targeting a wide range of people from Creative directors to the individual eg. bride

Industry/Entity Type

Business

Requirements
Must have
• Name: Delphine Hartwell
contact numbe 0417853120
email address:info@serafinaloire.com
website: www.serafinaloire.com
One of the images attached

professional makeup artist / hair stylist

I want it to show creativity
Nice to have
• logo, Double-sided card
Should not have
• the design should not use tradional style. Or images that are not my own

```html
<!DOCTYPE html>
<html lang="en">
<head>
<meta charset="utf-8">
<title>Serafina Loire – Business Card</title>
<link rel="stylesheet" href="https://fonts.googleapis.com/css2?family=Pinyon+Script&family=Arimo&display=swap">
<style>
  :root {
    --page: #ffffff;
    --card: #050505;
    --frame-light: #d8d8d8;
    --frame-mid: #8a8a8a;
    --panel: #bfbfbf;
    --photo-light: #d6d6d6;
    --photo-dark: #3a3a3a;
    --ink: #0a0a0a;
    --label: #222222;
  }
  * { margin: 0; padding: 0; box-sizing: border-box; }
  html, body { width: 1200px; height: 980px; overflow: hidden; background: var(--page); }
  .sheet { position: relative; width: 1200px; height: 980px; }

  .side-label {
    position: absolute; top: 14px; width: 200px; margin-left: -100px;
    text-align: center; font-family: "Arimo", Arial, sans-serif;
    font-size: 26px; color: var(--label);
  }
  .side-label--front { left: 302px; }
  .side-label--back { left: 921px; }

  .card {
    position: absolute; top: 73px; height: 887px;
    background: var(--card);
  }
  .card--front { left: 37px; width: 531px; }
  .card--back { left: 674px; width: 495px; }

  .card__frame {
    position: absolute; inset: 22px;
    border: 3px solid var(--frame-mid);
    box-shadow: 0 0 16px 3px rgba(210,210,210,.55), inset 0 0 22px 6px rgba(220,220,220,.7);
  }
  .card__panel {
    position: absolute; inset: 42px;
    border: 2px solid var(--frame-light);
    box-shadow: 0 0 14px 4px rgba(230,230,230,.7);
    overflow: hidden;
  }
  .card--back .card__panel { background: var(--panel); }
  .card__photo {
    position: absolute; inset: 0;
    background:
      radial-gradient(ellipse 55% 40% at 42% 38%, var(--photo-light), transparent 70%),
      linear-gradient(160deg, #9c9c9c 0%, var(--photo-dark) 55%, #6e6e6e 100%);
  }

  .script { font-family: "Pinyon Script", cursive; color: var(--ink); white-space: nowrap; }

  .front-name {
    position: absolute; left: 0; right: 0; bottom: 50px;
    text-align: center; font-size: 60px;
  }

  .details {
    position: absolute; left: 0; right: 0; top: 520px;
    text-align: center;
  }
  .details__name { font-size: 58px; line-height: 1.1; }
  .details__role { font-size: 32px; line-height: 1.2; margin-top: 4px; }
  .details__email { font-size: 22px; line-height: 1.2; margin-top: 12px; }
  .details__phone { font-size: 22px; line-height: 1.2; margin-top: 14px; }
</style>
</head>
<body>
<main class="sheet">
  <p class="side-label side-label--front">front</p>
  <p class="side-label side-label--back">back</p>

  <section class="card card--front">
    <div class="card__frame"></div>
    <div class="card__panel">
      <div class="card__photo" role="img" aria-label="Black and white portrait photograph of a woman with long wavy hair"></div>
      <p class="script front-name">Serafina Loire</p>
    </div>
  </section>

  <section class="card card--back">
    <div class="card__frame"></div>
    <div class="card__panel">
      <div class="details">
        <p class="script details__name">Serafina Loire</p>
        <p class="script details__role">Professional Makeup Artist</p>
        <p class="script details__email">info@serafinaloire.com</p>
        <p class="script details__phone">Contact Number 0417853120</p>
      </div>
    </div>
  </section>
</main>
</body>
</html>
```